Small environmental consultancy needs a simple but professional web design

We are a boutique environmental consultancyand contracting business located in Margaret River in the South West of Western Australia.

We have two arms
1) Consulting which offers environmental planning, management and assessment services primarily to local government and the development industry.
2) Contracting which implements on site plans and on ground works primarily involving revegetation, bush regeneration and environmental weed control.

We need a simple yet professional web design within the wordpress platform that commmunicates professionalism, experience and technical expertise without appearing too corporate.

Something like this structure appeals:
http://verdantia.net.au/environment-services/
or
http://www.ridgefallenvironmental.com.au/index.php

(without the image gallery function)

Target Market(s)

Local Government Officers deciding on tenders;
Developers, Engineers, Town Planning consultants looking for environmental expertise

Industry/Entity Type

Business

Number of Pages Required

5+ page

Font styles to use
Sans Serif

Colors
33a6d7
9bcb3c

Requirements
Must have
• Pages required include:
• Home
• Environmental Planning and Management
• Revegetation and Regeneration Implementation (This page can mirror the Environmental Planning and Management page exactly in structure but with different text and images)
• About Us (I think that this page can be relatively simple and generic)
• Contact (I think that this page can be very simple and generic)
Nice to have
• An ability to start out basic and quicikly establish a website presence and then build in additional drop downs and pages over time.
Should not have
• It does not need a photo gallery page;
• It does not need a major amount of space dedicated to social media and blogs etc as this is not currently particularly active area for us

```html
<!DOCTYPE html>
<html lang="en">
<head>
<meta charset="utf-8">
<title>Logo – Environmental Consultancy</title>
<link href="https://fonts.googleapis.com/css2?family=Lato:wght@300;400;700;900&family=Roboto:wght@400;500;700&display=swap" rel="stylesheet">
<style>
:root{
  --green:#8dc63f;
  --green-dark:#6fa82a;
  --green-head:#86c440;
  --sky:#8dd4f3;
  --footer:#5cb9e0;
  --footer-deep:#4aa7d2;
  --nav:#23272b;
  --nav-top:#34393e;
  --ink:#222;
  --grey:#8a8a8a;
  --grey-light:#9a9a9a;
  --white:#fff;
}
*{margin:0;padding:0;box-sizing:border-box}
html,body{width:1195px;height:1200px;overflow:hidden;background:var(--white)}
body{position:relative;font-family:"Lato",Arial,sans-serif;color:var(--ink)}
.abs{position:absolute}

/* header */
.brand{left:205px;top:16px;font:400 41px/1 "Lato",sans-serif;color:#555}
.head-contact{display:flex;align-items:center;gap:8px;font:700 11px/15px "Roboto",sans-serif;color:#222}
.head-contact.phone{left:716px;top:18px}
.head-contact.mail{left:855px;top:20px}
.head-contact .light{font-weight:400}

/* nav */
.nav-bar{left:0;top:82px;width:1195px;height:34px;background:linear-gradient(var(--nav-top),var(--nav))}
.nav-item{top:82px;height:34px;font:700 12.5px/34px "Roboto",sans-serif;color:var(--white);text-align:center}
.nav-sep{top:82px;width:1px;height:34px;background:#444a50}
.nav-tab{top:73px;height:43px;background:var(--green);color:#1d2a10;font:500 11.5px/14px "Roboto",sans-serif;padding:8px 0 0 11px;border-radius:3px 3px 0 0;white-space:nowrap;overflow:hidden}

/* hero */
.hero-title{left:206px;top:154px;font:700 32px/37px "Lato",sans-serif;color:var(--green-head)}
.hero-text{left:210px;top:278px;width:300px;font:400 12.5px/16px "Lato",sans-serif;color:var(--grey-light)}
.hero-photo{left:0;top:0}

/* about band */
.about-band{left:0;top:385px;width:1195px;height:149px;background:var(--sky)}
.region-map{left:215px;top:358px;width:220px;height:204px;background:linear-gradient(90deg,#3a9a3a 0%,#6aa36a 35%,#a0a0a0 55%,#9d9d9d 100%)}
.about-title{left:469px;top:414px;font:300 33px/1 "Lato",sans-serif;color:#1f2a30}
.about-text{left:469px;top:456px;width:545px;font:400 12.5px/15px "Lato",sans-serif;color:#1f2a30}
.btn-more{left:469px;top:494px;width:51px;height:19px;background:var(--white);border-radius:2px;font:500 10px/19px "Roboto",sans-serif;text-align:center;color:#222}

/* services */
.service{top:578px;width:190px;text-align:center}
.service-img{width:152px;height:134px;margin:0 auto}
.service-title{margin-top:16px;font:400 14.5px/17px "Roboto",sans-serif;color:#222;letter-spacing:.2px}
.service-text{margin:13px auto 0;width:172px;font:400 12.5px/16.5px "Roboto",sans-serif;color:var(--grey)}

/* footer */
.footer{left:0;top:885px;width:1195px;height:315px;background:linear-gradient(180deg,var(--footer) 0%,var(--footer-deep) 100%)}
.talk{left:210px;top:921px;font:300 21px/25px "Lato",sans-serif;color:var(--white)}
.foot-contact{font:700 16px/23px "Lato",sans-serif;color:var(--white)}
.foot-contact .light{font-weight:300}
.btn-contact{left:890px;top:927px;width:104px;height:38px;background:linear-gradient(#9bd04a,var(--green-dark));border-radius:3px;font:700 11px/38px "Lato",sans-serif;color:var(--white);text-align:center}
.foot-rule{left:150px;top:983px;width:882px;height:1px;background:rgba(255,255,255,.35)}
.foot-col h3{font:400 15px/1 "Roboto",sans-serif;color:var(--white);margin-bottom:14px}
.foot-col li{list-style:none;font:400 10.5px/12px "Roboto",sans-serif;color:var(--white);margin-bottom:7.5px}
.foot-brand{left:702px;top:1033px;font:400 43px/1 "Roboto",sans-serif;color:var(--white)}
.foot-text{left:703px;top:1082px;width:270px;font:400 10.5px/12.5px "Roboto",sans-serif;color:var(--white)}
.copyright{left:680px;top:1161px;font:400 11px/1 "Roboto",sans-serif;color:var(--white)}
</style>
</head>
<body>

<!-- header -->
<div class="abs brand">Logo</div>
<div class="abs head-contact phone">
  <svg width="36" height="28" viewBox="0 0 36 28"><path d="M3 9c0-5 8-7 15-7s15 2 15 7v3h-8V9c-3-1-11-1-14 0v3H3z" fill="#5cb9e0"/><path d="M9 12h18l4 14H5z" fill="#5cb9e0"/><circle cx="18" cy="19" r="4" fill="#fff"/></svg>
  <div>028 90 000 147<br>1800 555 019</div>
</div>
<div class="abs head-contact mail">
  <svg width="32" height="22" viewBox="0 0 32 22"><rect x="1" y="1" width="30" height="20" fill="#5cb9e0"/><path d="M1 1l15 11L31 1M1 21l11-10M31 21L20 11" stroke="#fff" stroke-width="1.5" fill="none"/></svg>
  <div><span class="light">enviroment@</span><br>Companysite.com</div>
</div>

<!-- navigation -->
<div class="abs nav-bar"></div>
<div class="abs nav-sep" style="left:205px"></div>
<div class="abs nav-item" style="left:205px;width:98px">HOME</div>
<div class="abs nav-sep" style="left:303px"></div>
<div class="abs nav-item" style="left:303px;width:112px">ABOUT US</div>
<div class="abs nav-sep" style="left:415px"></div>
<div class="abs nav-item" style="left:415px;width:134px">CONTACT US</div>
<div class="abs nav-tab" style="left:562px;width:200px;padding-left:21px">ENVIRONMENTAL PLANNING<br>AND MANAGEMENT</div>
<div class="abs nav-tab" style="left:771px;width:223px">REVEGETATION AND REGENERATION<br>IMPLEMENTATION</div>

<!-- hero -->
<h1 class="abs hero-title">Serving Government<br>and Commercial<br>Clients</h1>
<p class="abs hero-text">Lorem ipsum dolor sit amet, consectetur adipiscing elit, sed do eiusmod tempor incididunt ut labore.</p>
<svg class="abs hero-photo" width="1195" height="385" viewBox="0 0 1195 385" role="img" aria-label="Photo of a coastal estuary with dunes and a scrub-covered hill under blue sky">
  <defs>
    <clipPath id="hero-clip"><rect x="0" y="116" width="1195" height="269"/></clipPath>
    <linearGradient id="hero-tones" x1="0" y1="0" x2="0" y2="1">
      <stop offset="0" stop-color="#5aa9ea"/>
      <stop offset=".33" stop-color="#8cc3f0"/>
      <stop offset=".4" stop-color="#3f5a35"/>
      <stop offset=".58" stop-color="#556b3c"/>
      <stop offset=".66" stop-color="#d9cfb0"/>
      <stop offset=".74" stop-color="#3c5f8f"/>
      <stop offset="1" stop-color="#2c4a7c"/>
    </linearGradient>
  </defs>
  <circle cx="781" cy="262" r="249" fill="url(#hero-tones)" clip-path="url(#hero-clip)"/>
</svg>

<!-- about band -->
<div class="abs about-band"></div>
<div class="abs region-map" role="img" aria-label="Map of Australia with Western Australia highlighted in green and a location pin"></div>
<h2 class="abs about-title">About us</h2>
<p class="abs about-text">Lorem ipsum dolor sit amet, consectetur adipiscing elit, sed do eiusmod tempor incididunt ut labore et dolore magna aliqua. Ut enim ad minim veniam, quis nostrud exercitation ullamco.</p>
<div class="abs btn-more">MORE +</div>

<!-- services -->
<div class="abs service" style="left:196px">
  <div class="service-img" role="img" aria-label="GIS map of catchment areas" style="background:linear-gradient(135deg,#e9c38a,#a8c89a 50%,#e6b070)"></div>
  <div class="service-title">GIS MAPPING<br>AND ANALYSIS</div>
  <p class="service-text">Lorem ipsum dolor sit amet, consectetur adipiscing elit, sed do eiusmod tempor incididunt ut labore et dolore magna aliqua.</p>
</div>
<div class="abs service" style="left:399px">
  <div class="service-img" role="img" aria-label="Aerial photo of an orange river through polluted land" style="background:linear-gradient(135deg,#5d7a3a,#c9a98c 45%,#e07b16 60%,#c24a1a)"></div>
  <div class="service-title">ENVIRONMENTAL<br>IMPACT ASSESSMENT</div>
  <p class="service-text">Sed ut perspiciatis unde omnis iste natus error sit voluptatem accusantium doloremque laudantium, totam rem aperiam.</p>
</div>
<div class="abs service" style="left:605px">
  <div class="service-img" role="img" aria-label="Photo of cacti and dry native vegetation" style="background:linear-gradient(180deg,#7fa7c9,#9fb5c2 40%,#8a7048 75%,#6a5432)"></div>
  <div class="service-title">NATIVE VEGETATION<br>CLEARING PERMITS</div>
  <p class="service-text">I must explain to you how all this mistaken idea of denouncing pleasure and praising pain was born and I will give you a complete.</p>
</div>
<div class="abs service" style="left:812px">
  <div class="service-img" role="img" aria-label="Photo of a botanist surveying a flowering garden" style="background:linear-gradient(180deg,#3c6a2a,#5c8a3a 50%,#8a7fb0 80%,#4a6a30)"></div>
  <div class="service-title">ETHNO BOTANICAL<br>SURVEYS</div>
  <p class="service-text">At vero eos et accusamus et iusto odio dignissimos ducimus qui blanditiis praesentium voluptatum deleniti atque corrupti quos dolores.</p>
</div>

<!-- footer -->
<footer class="abs footer" role="img" aria-label="Faded photo of a tree-lined country path behind the footer"></footer>
<div class="abs talk">Talk to our cuctomer<br>services team today...</div>
<svg class="abs" style="left:414px;top:918px" width="58" height="46" viewBox="0 0 58 46"><path d="M3 15C3 6 17 2 29 2s26 4 26 13v5H42v-5c-6-2-20-2-26 0v5H3z" fill="#fff"/><path d="M14 20h30l7 24H7z" fill="#fff"/><circle cx="29" cy="32" r="7" fill="#5cb9e0"/></svg>
<div class="abs foot-contact" style="left:486px;top:922px">028 90 000 147<br>1800 555 019</div>
<svg class="abs" style="left:640px;top:926px" width="54" height="38" viewBox="0 0 54 38"><rect x="1.5" y="1.5" width="51" height="35" fill="none" stroke="#fff" stroke-width="3"/><path d="M2 2l25 19L52 2M2 36l19-17M52 36L33 19" stroke="#fff" stroke-width="2.5" fill="none"/></svg>
<div class="abs foot-contact" style="left:711px;top:922px"><span class="light">enviroment@</span><br>Companysite.com</div>
<div class="abs btn-contact">CONTACT US</div>
<div class="abs foot-rule"></div>

<nav class="abs foot-col" style="left:212px;top:1023px">
  <h3>Navigation</h3>
  <ul>
    <li>Home</li>
    <li>Environmental Planning<br>and Management</li>
    <li>Revegetation and<br>Regeneration Implementation</li>
    <li>About Us</li>
    <li>Contact</li>
  </ul>
</nav>
<div class="abs foot-col" style="left:417px;top:1023px">
  <h3>Education</h3>
  <ul>
    <li>Marine Activities</li>
    <li>River/Estuary</li>
    <li>Bush Activities</li>
    <li>AusVELS, VET,VCAL and VCE</li>
    <li>School holiday programs</li>
    <li>Harbour Point Lighthouse Tour</li>
  </ul>
</div>
<div class="abs foot-brand">LOGO</div>
<p class="abs foot-text">Lorem ipsum dolor sit amet, consec tuer adipiscing elit, sed diam nonum nibh euismod.Lotuer adipiscing elit, sed diam nibh eu.</p>
<div class="abs copyright">Copyright 2013-2015 Logo Co., Ltd., All Rights Reserved</div>

</body>
</html>
```